Homes, Invest in Non-performing loans

We need only 3 web pages, one for the home, one for the content, one for the properties.
The main focus of our business is to offer non performing loans (before foreclosures) to the general public. All the non-performing mortgages will end in a house, an apartment, a store, etc.
Our customers are able to invest from 10,000usd to 1,000,000usd (average 50,000usd).
Our customers' usual focus groups are employees who want second earnings, perceiving the business feeling without outlay time. They look for a solid finance sense corporation that confers them certainty.
Nearly all our clients desire the house, apartment, store, etc. more than the actual earnings.
The name of our company is BRAMLEY
Reason: We value the time and effort you already invest in our project. We realize that we did't come back on some of the doubts requested by the designers. It will be inequitable to the designers who prerequisite our feedback. We also appreciate the comprehension of the community in this postponement.
Reason: Designers,
We really apreciate all the time and effort you put on our project. From the begining we ask for 3 pages, so now we will leave the 10 finalist and provide some extra time to submit the other 2 pages.
We will race the price in 10%
Target Market(s)
Our customers average investors works as employees and want to have a second income or business without spending time. (People from 35 to 50)
Industry/Entity Type
Finance
Requirements
Should not have
- FLASH

```html
<!DOCTYPE html>
<html lang="en">
<head>
<meta charset="utf-8">
<title>Bramley — Remates Hipotecarios</title>
<link href="https://fonts.googleapis.com/css2?family=Open+Sans:wght@400;600;700;800&display=swap" rel="stylesheet">
<style>
:root{
  --page:#fbe8b4;
  --page-light:#fdf2d2;
  --topbar:#3a3a3a;
  --olive:#8a8a2e;
  --olive-dark:#6f7020;
  --text:#333333;
  --muted:#666666;
  --link:#1d4f8c;
  --blue:#1f7fd6;
  --blue-dark:#1457a3;
  --card:#ffffff;
  --card-edge:#f3dfa2;
  --rule:#cfcfcf;
  --footer:#f5f5f5;
}
*{box-sizing:border-box;margin:0;padding:0}
html,body{width:1051px;height:1200px;overflow:hidden}
body{background:var(--page);font-family:"Open Sans",Arial,sans-serif;color:var(--text);position:relative}
a{color:inherit}

.topbar{position:absolute;left:0;top:0;width:1051px;height:26px;background:linear-gradient(#4a4a4a,#2c2c2c);color:#fff;font-size:13px}
.topbar .bookmark{position:absolute;left:52px;top:4px}
.topbar .bookmark a{text-decoration:underline}
.topbar .sep{margin:0 6px;opacity:.8}
.topbar .greet{position:absolute;left:570px;top:4px}
.newsletters{position:absolute;left:641px;top:2px;width:247px;height:22px;background:#fff;color:#222;font-size:13px;padding:2px 8px;border:1px solid #999}
.newsletters svg{position:absolute;right:1px;top:1px}
.topbar .auth{position:absolute;left:900px;top:4px}
.topbar .auth a{text-decoration:underline;margin-right:17px}

.header{position:absolute;left:0;top:26px;width:1051px;height:129px;background:linear-gradient(90deg,var(--page-light),var(--page))}
.brand{position:absolute;left:54px;top:50px;display:flex;align-items:center;gap:10px}
.brand .mark{width:28px;height:28px;background:var(--olive)}
.brand .name{font-size:40px;font-weight:800;color:#3a3a3a;letter-spacing:1px;line-height:1}
.tagline{position:absolute;left:54px;top:101px;font-size:8px;letter-spacing:1.5px;color:#444}
.callus{position:absolute;left:698px;top:32px;width:134px;height:62px;background:linear-gradient(#3aa0ec,var(--blue-dark));color:#fff;text-align:center;border-radius:2px}
.callus .label{font-size:13px;font-weight:700;margin-top:10px;display:block}
.callus .number{font-size:23px;font-weight:700;display:block;line-height:26px}
.callus-shadow{position:absolute;left:660px;top:94px;width:210px;height:6px;background:radial-gradient(ellipse at top,rgba(0,0,0,.25),transparent 70%)}

.nav{position:absolute;left:0;top:155px;width:1051px;height:30px;background:linear-gradient(#9a9a3a,var(--olive-dark));border-top:1px solid #b5b55a}
.nav ul{list-style:none;display:flex;position:absolute;left:32px;top:0;height:29px}
.nav li{color:#fff;font-weight:700;font-size:13px;line-height:29px;text-align:center;border-left:1px solid #a8a84d;border-right:1px solid #6a6a1e}
.search{position:absolute;left:787px;top:5px;width:223px;height:20px;background:#fff;font-size:12px;color:#999;padding:1px 10px}
.search svg{position:absolute;right:8px;top:3px}

.slider{position:absolute;left:31px;top:214px;width:989px;height:351px;background:#fff;border:1px solid var(--card-edge);padding:9px}
.slide{position:relative;width:969px;height:330px;background:linear-gradient(#3b7fd0 0%,#8fc0ec 45%,#a9d58a 62%,#4fa82a 80%,#3f9320 100%)}
.motto{position:absolute;left:25px;top:228px;font-size:68px;font-weight:600;color:#fff;letter-spacing:-1px;text-shadow:0 2px 4px rgba(0,0,0,.3)}
.dots{position:absolute;left:462px;top:569px;display:flex;gap:6px}
.dots span{width:21px;height:21px;border-radius:50%;background:radial-gradient(circle at 40% 35%,#eee,#bbb)}
.dots span.active{background:radial-gradient(circle at 40% 35%,#5aa2e0,#1b5fa6)}

.card{position:absolute;top:609px;width:235px;height:391px;background:var(--card);border:1px solid var(--card-edge);padding:18px 9px 0}
.card h2{font-size:17px;font-weight:600;color:#333;padding-bottom:5px;border-bottom:1px solid var(--rule);white-space:nowrap}
.thumb{margin-top:19px;width:216px;height:82px;border:1px solid #ccc}
.thumb.map{background:linear-gradient(135deg,#d9e4c0,#e8e1c8 50%,#a9c0d6)}
.thumb.flats{background:linear-gradient(#6fa3e6 0%,#bcd6f0 35%,#9a5a3e 55%,#7a6a5a 100%)}
.thumb.house{background:linear-gradient(#4f8fe0 0%,#c2dcf4 50%,#69b53a 75%,#3f8f1f 100%)}
.thumb.rates{background:radial-gradient(circle at 25% 50%,#2c6cc7 0 25%,transparent 26%),linear-gradient(90deg,#fff,#dfe8f6);}
.states{list-style:none;margin-top:14px;padding-left:3px}
.states li{font-size:12px;letter-spacing:.8px;color:var(--link);line-height:19.5px}
.states li a{border-bottom:1px solid var(--link);text-decoration:none}
.copy{margin-top:20px;padding-left:3px;font-size:11.5px;letter-spacing:.8px;line-height:19.5px;color:#222}
.copy a{color:var(--link)}
.rates-table{margin-top:16px;width:216px;border-collapse:collapse;font-size:11.5px;letter-spacing:.7px}
.rates-table th{text-align:left;font-weight:400;color:var(--muted);padding:0 0 6px;border-bottom:1px solid var(--rule)}
.rates-table td{padding:5px 0 4px;border-bottom:1px solid var(--rule);color:var(--link)}
.rates-table td.rate{color:#444;width:62px}
.readmore{position:absolute;left:9px;bottom:25px;width:124px;height:25px;background:linear-gradient(#3ea2ee,var(--blue-dark));color:#fff;font-weight:700;font-size:13px;text-align:center;line-height:25px;border:1px solid #1b5aa0}

.footer{position:absolute;left:32px;top:1017px;width:987px;height:162px;background:var(--footer);border:1px solid var(--card-edge);padding:17px 21px}
.footer .row{font-size:11.5px;line-height:23.7px;display:flex;align-items:center}
.footer .row strong{font-size:12.5px;font-weight:700;margin-right:10px;letter-spacing:.3px}
.footer .row span.item + span.item::before{content:"|";margin:0 8px;color:#555}
.social{display:flex;gap:9px}
.social span{width:18px;height:18px;background:#2b5a8a;display:inline-block}
</style>
</head>
<body>
<div class="topbar">
  <div class="bookmark">Bookmark <a>this page</a><span class="sep">|</span><a>this site</a></div>
  <div class="greet">Hi, Guest</div>
  <div class="newsletters">View Newsletters
    <svg width="14" height="18" viewBox="0 0 14 18"><rect width="14" height="18" fill="#ddd"/><path d="M3 7h8l-4 5z" fill="#333"/></svg>
  </div>
  <div class="auth"><a>Sign In</a><a>Register</a></div>
</div>

<header class="header">
  <div class="brand"><span class="mark"></span><span class="name">BRAMLEY</span></div>
  <div class="tagline">REMATES HIPOTECARIOS</div>
  <div class="callus"><span class="label">Call us today</span><span class="number">55 20 41 17</span></div>
  <div class="callus-shadow"></div>
</header>

<nav class="nav">
  <ul>
  <li style="width:86px">HOME</li>
  <li style="width:94px">SEMPER</li>
  <li style="width:114px">NUSQUAM</li>
  <li style="width:91px">LEGERE</li>
  <li style="width:113px">ELECTRAM</li>
  <li style="width:143px">OMNIUS REBUS</li>
  <li style="width:106px">CONTACT</li>
  </ul>
  <div class="search">Search
    <svg width="14" height="14" viewBox="0 0 14 14"><circle cx="6" cy="6" r="4.5" fill="none" stroke="#999" stroke-width="2"/><path d="M9 9l4 4" stroke="#999" stroke-width="2.5"/></svg>
  </div>
</nav>

<section class="slider">
  <div class="slide" role="img" aria-label="Brick house with a red tiled roof on a green hill under a blue sky with clouds">
    <div class="motto">Motto goes here</div>
  </div>
</section>
<div class="dots"><span></span><span class="active"></span><span></span><span></span><span></span></div>

<article class="card" style="left:32px">
  <h2>Find property using a map</h2>
  <div class="thumb map" role="img" aria-label="Road map of the eastern United States"></div>
  <ul class="states">
    <li><a>Alabama</a></li><li><a>Alaska</a></li><li><a>American Samoa</a></li><li><a>Arizona</a></li>
    <li><a>Arkansas</a></li><li><a>California</a></li><li><a>Colorado</a></li><li><a>Connecticut</a></li>
  </ul>
  <div class="readmore">Read more</div>
</article>

<article class="card" style="left:283px">
  <h2>Title Two Goes Here</h2>
  <div class="thumb flats" role="img" aria-label="Row of brick apartment buildings"></div>
  <p class="copy"><a>Suas dicam iriure</a> id vix, duo ex reque appetere. An vis perfecto praesent consequuntur, ius ex quis atomorum vituperatoribus. Eum <a>alterum fuisset</a> adolescens eu. Vim appellantur accommodare disputationi ei, aeterno <a>signiferumque eam in</a>.</p>
  <div class="readmore">Read more</div>
</article>

<article class="card" style="left:534px">
  <h2>Title Three Goes Here</h2>
  <div class="thumb house" role="img" aria-label="House with a red roof on a green field"></div>
  <p class="copy"><a>Suas dicam iriure</a> id vix, duo ex reque appetere. An vis perfecto praesent consequuntur, ius ex quis atomorum vituperatoribus. Eum <a>alterum fuisset</a> adolescens eu. Vim appellantur accommodare disputationi ei, aeterno <a>signiferumque eam in</a>.</p>
  <div class="readmore">Read more</div>
</article>

<article class="card" style="left:785px">
  <h2>Credit Rates</h2>
  <div class="thumb rates" role="img" aria-label="Blue finance icons: calculator, currency, cards and charts"></div>
  <table class="rates-table">
    <tr><th colspan="2">Type</th></tr>
    <tr><td>Balance Transfer</td><td class="rate">12.95%</td></tr>
    <tr><td>Low Interest</td><td class="rate">12.95%</td></tr>
    <tr><td>Cash Back</td><td class="rate">12.95%</td></tr>
    <tr><td>Rewards</td><td class="rate">12.95%</td></tr>
    <tr><td>Business</td><td class="rate">12.95%</td></tr>
  </table>
  <div class="readmore">Read more</div>
</article>

<footer class="footer">
  <div class="row"><strong>MY ACCOUNT:</strong><span class="item">Sign In</span><span class="item">Register</span></div>
  <div class="row"><strong>FOLLOW BRAMLEY:</strong><span class="social"><span></span><span></span><span></span></span></div>
  <div class="row"><strong>ABOUT:</strong><span class="item">Reformidans luvaret</span><span class="item">Consequuntur</span><span class="item">Ullamcorper Essent</span><span class="item">Gloriatur Dicam</span><span class="item">Primis Scriptorem</span><span class="item">Nulla Dolore</span><span class="item">Aliquando</span><span class="item">Reformidans luvaret</span></div>
  <div class="row"><strong>SERVICES:</strong><span class="item">Gloriatur Dicam</span><span class="item">Primis Scriptorem</span><span class="item">Nulla Dolore</span><span class="item">Aliquando</span><span class="item">Reformidans luvaret</span><span class="item">Consequuntur</span></div>
  <div class="row"><strong>TOOLS:</strong><span class="item">Reformidans luvaret</span><span class="item">Consequuntur</span><span class="item">Ullamcorper Essent</span><span class="item">Gloriatur Dicam</span><span class="item">Primis Scriptorem</span><span class="item">Nulla Dolore</span><span class="item">Aliquando</span></div>
</footer>
</body>
</html>
```